Solar energy proposal for homeowners

I am providing households with solar energy proposals, and I need a high-quality brochure that is packaged cleverly to attract the homeowner's attention. Take a look at the one page solar brochure that I have included to get an idea of text and content.

Target Market(s)

Residential Homeowners

Industry/Entity Type

Solar

Requirements
Must have
• High quality document

```html
<!DOCTYPE html>
<html lang="en">
<head>
<meta charset="utf-8">
<title>Helivolt Energy – Solar for $0 Down</title>
<link rel="stylesheet" href="https://fonts.googleapis.com/css2?family=Archivo:wght@500;600;700;800&family=Inter:wght@400;500;600&display=swap">
<style>
  :root {
    --page-bg: #eeeeee;
    --sky-top: #1f72d4;
    --sky-mid: #2891d3;
    --sky-low: #27adc0;
    --sky-base: #2cb9c6;
    --lime: #bddf34;
    --lime-card: #badc3c;
    --band-green: #63c63c;
    --ink: #161a14;
    --white: #ffffff;
  }
  * { box-sizing: border-box; margin: 0; padding: 0; }
  html, body { width: 1200px; height: 1200px; overflow: hidden; }
  body {
    background: var(--page-bg);
    font-family: "Inter", Arial, sans-serif;
    position: relative;
  }
  .flyer {
    position: absolute;
    left: 176px; top: 0;
    width: 848px; height: 1200px;
    overflow: hidden;
    color: var(--white);
  }
  .flyer-photo {
    position: absolute; inset: 0;
    background:
      radial-gradient(ellipse 220px 300px at 700px 580px, rgba(150,215,235,0.35), rgba(150,215,235,0) 70%),
      linear-gradient(180deg, var(--sky-top) 0%, var(--sky-mid) 32%, var(--sky-low) 68%, var(--sky-base) 100%);
  }
  .brand {
    position: absolute; left: 48px; top: 62px;
    display: flex; align-items: center; gap: 16px;
    font-family: "Archivo", Arial, sans-serif;
    font-weight: 500; font-size: 50px; letter-spacing: -0.5px;
    color: var(--white);
  }
  .brand-mark { width: 58px; height: 58px; background: var(--white); }
  .headline-band {
    position: absolute; left: 0; top: 178px;
    width: 622px; height: 310px;
    background: linear-gradient(90deg, var(--band-green) 0%, rgba(86,196,90,0.92) 45%, rgba(60,190,150,0.55) 80%, rgba(50,180,170,0.2) 100%);
  }
  .headline {
    position: absolute; left: 48px; top: 196px;
    font-family: "Archivo", Arial, sans-serif;
    font-weight: 700; font-size: 53px; line-height: 69px;
    letter-spacing: 0.3px; text-transform: uppercase;
  }
  .tagline {
    position: absolute; left: 48px; top: 500px;
    font-size: 26px; line-height: 36px; font-weight: 400;
  }
  .section-label {
    position: absolute;
    display: inline-block;
    background: var(--lime);
    color: var(--ink);
    font-family: "Archivo", Arial, sans-serif;
    font-weight: 600; font-size: 32px; line-height: 42px;
    padding: 0 6px;
  }
  .about-label { left: 48px; top: 608px; }
  .why-label { left: 503px; top: 608px; }
  .about-text {
    position: absolute; left: 48px; top: 661px; width: 440px;
    font-size: 14px; line-height: 18px;
  }
  .why-list {
    position: absolute; left: 506px; top: 667px;
    list-style: none; font-size: 14px; line-height: 17px;
  }
  .why-list li::before { content: "• "; }
  .service-card {
    position: absolute; left: 71px; top: 797px;
    width: 709px; height: 320px;
    background: var(--lime-card);
    border-radius: 18px;
    color: var(--ink);
  }
  .service-title {
    position: absolute; left: 0; right: 0; top: 16px;
    text-align: center;
    font-family: "Archivo", Arial, sans-serif;
    font-weight: 600; font-size: 32px;
  }
  .service-rule {
    position: absolute; left: 190px; top: 60px;
    width: 328px; height: 2px; background: var(--ink);
  }
  .service-cross-v {
    position: absolute; left: 354px; top: 62px;
    width: 1px; height: 250px;
    background: linear-gradient(180deg, rgba(22,26,20,0) 0%, var(--ink) 50%, rgba(22,26,20,0) 100%);
  }
  .service-cross-h {
    position: absolute; left: 280px; top: 193px;
    width: 150px; height: 1px;
    background: linear-gradient(90deg, rgba(22,26,20,0) 0%, var(--ink) 50%, rgba(22,26,20,0) 100%);
  }
  .service-item { position: absolute; width: 270px; }
  .service-item svg {
    position: absolute; left: -52px; top: -2px;
    width: 40px; height: 40px;
    fill: none; stroke: var(--ink); stroke-width: 1.8;
    stroke-linecap: round; stroke-linejoin: round;
  }
  .service-item h3 {
    font-family: "Inter", Arial, sans-serif;
    font-size: 13px; font-weight: 600; margin-bottom: 14px;
  }
  .service-item p { font-size: 13.5px; line-height: 18px; }
  .item-affordable { left: 78px; top: 82px; }
  .item-install { left: 432px; top: 82px; }
  .item-local { left: 78px; top: 214px; }
  .item-eco { left: 432px; top: 214px; }
  .contact-bar {
    position: absolute; left: 89px; right: 86px; top: 1146px;
    display: flex; justify-content: space-between;
    font-size: 16px;
  }
  .contact-address { margin-left: -40px; margin-right: auto; padding-left: 66px; }
</style>
</head>
<body>
  <main class="flyer">
    <div class="flyer-photo" role="img" aria-label="Aerial photo of rooftop solar panels with two installers in hard hats and safety vests"></div>

    <div class="brand"><span class="brand-mark"></span>Helivolt Energy</div>

    <div class="headline-band"></div>
    <h1 class="headline">Solar for $0<br>down.<br>No liens.<br>No kidding.</h1>

    <p class="tagline">Power Your Future with<br>Helivolt Energy</p>

    <h2 class="section-label about-label">About Us</h2>
    <p class="about-text">At Helivolt Energy, our mission is to make solar simple and accessible for everyone. No high-pressure sales-just the information you need to make a smart choice. With our solar rental program, you can lower your monthly energy costs and pay less current electricity bill.</p>

    <h2 class="section-label why-label">Why Choose Us?</h2>
    <ul class="why-list">
      <li>No financing</li>
      <li>No liens</li>
      <li>No down payment</li>
      <li>No insurance costs</li>
      <li>No long-term commitment</li>
      <li>No maintenance costs</li>
    </ul>

    <section class="service-card">
      <h2 class="service-title">Our Best Service</h2>
      <div class="service-rule"></div>
      <div class="service-cross-v"></div>
      <div class="service-cross-h"></div>

      <div class="service-item item-affordable">
        <svg viewBox="0 0 40 40" aria-hidden="true">
          <path d="M20 9a9 9 0 0 0-5 16.5V29h10v-3.5A9 9 0 0 0 20 9z"/>
          <path d="M16 32h8M17 35h6M20 3v2M8 8l1.5 1.5M32 8l-1.5 1.5M4 20h2M34 20h2"/>
        </svg>
        <h3>Affordable &amp; Transparent</h3>
        <p>Simple pricing, no hidden fees and a fixed monthly rate lower installation, maintenance, and than typical energy bills.</p>
      </div>

      <div class="service-item item-install">
        <svg viewBox="0 0 40 40" aria-hidden="true">
          <path d="M15 4h4l1 3 3 1.5 3-1.5 3 3-1.5 3 1 2.5 3 1v4l-3 1"/>
          <circle cx="17" cy="17" r="5"/>
          <circle cx="25" cy="26" r="8"/>
          <path d="M21.5 26l2.5 2.5 4.5-5"/>
          <path d="M9 25l-3 1.5-2-3 2-2.5-.5-3-3-1v-4l3-1 1.5-3"/>
        </svg>
        <h3>Expert Installation</h3>
        <p>Certified professionals handle installation, maintenance, and repairs end to end.</p>
      </div>

      <div class="service-item item-local">
        <svg viewBox="0 0 40 40" aria-hidden="true">
          <circle cx="19" cy="21" r="14"/>
          <circle cx="19" cy="21" r="8"/>
          <circle cx="19" cy="21" r="2.5"/>
          <path d="M19 21L33 7M29 6h4v4"/>
        </svg>
        <h3>Local Expertise</h3>
        <p>Florida-based team that understands the needs of Orlando and statewide homeowners.</p>
      </div>

      <div class="service-item item-eco">
        <svg viewBox="0 0 40 40" aria-hidden="true">
          <path d="M8 34c2-12 8-18 22-22-2 12-8 18-22 22z"/>
          <path d="M8 34C6 26 8 18 16 14c-1 8-4 14-8 20z"/>
          <path d="M10 32l14-14"/>
        </svg>
        <h3>Eco-Friendly</h3>
        <p>Clean, renewable solar energy that helps reduce your carbon footprint.</p>
      </div>
    </section>

    <footer class="contact-bar">
      <span class="contact-phone">(407)555-0142</span>
      <span class="contact-address">123 Anywhere St., Any City</span>
      <span class="contact-web">www.helivoltenergy.com</span>
    </footer>
  </main>
</body>
</html>
```